New Flyer Design Project Brenwick Doors and Interiors

Real photos will be added but please start with these for layout. Copy will be supplied so you can just leave a text box to start I am open to suggestions. Thank you

Target Market(s)

Builders, Designers, remodelers, consumers

Colors

Designer to choose colors to be used in the design.

Requirements
Must have
• Before and after photos, email, phone, logo, description

```html
<!DOCTYPE html>
<html lang="en">
<head>
<meta charset="utf-8">
<title>Brenwick Doors and Interiors – Flyer</title>
<link href="https://fonts.googleapis.com/css2?family=Oswald:wght@700&family=Lato:wght@400;700&display=swap" rel="stylesheet">
<style>
  :root {
    --brand-blue: #1d5fa6;
    --brand-blue-dark: #17518f;
    --ink: #333333;
    --logo-grey: #3b3b3b;
    --frame-grey: #9a9a9a;
    --paper: #ffffff;
    --backdrop: #e9ecef;
  }
  * { box-sizing: border-box; margin: 0; padding: 0; }
  html, body {
    width: 1200px; height: 1200px; overflow: hidden;
    background: var(--backdrop);
  }
  .canvas { position: relative; width: 1200px; height: 1200px; }
  .flyer {
    position: absolute; left: 149px; top: 17px;
    width: 842px; height: 1089px;
    background: var(--paper);
    transform: scale(1.07); transform-origin: top left;
    font-family: "Lato", sans-serif; color: var(--ink);
    box-shadow: 0 4px 18px rgba(0,0,0,0.18);
  }
  .headline-band {
    position: absolute; left: 0; top: 0; width: 411px; height: 119px;
    background: var(--brand-blue);
  }
  .headline, .logo-name {
    position: absolute; top: 30px;
    font-family: "Oswald", sans-serif; font-weight: 700;
    font-size: 60px; line-height: 80px; letter-spacing: 0.5px;
  }
  .headline { left: 36px; color: #fff; }
  .logo-name { left: 476px; color: var(--logo-grey); }

  .tag {
    position: absolute; left: 40px; height: 30px;
    background: var(--brand-blue); color: #fff;
    font-size: 19px; font-weight: 700; line-height: 30px;
    padding-left: 7px;
    clip-path: polygon(0 0, calc(100% - 14px) 0, 100% 100%, 0 100%);
  }
  .tag-about { top: 154px; width: 131px; }
  .tag-services { top: 541px; width: 125px; }

  .about-text {
    position: absolute; left: 40px; top: 192px; width: 357px;
    font-size: 18.4px; line-height: 23.1px; text-align: justify;
  }

  .services {
    position: absolute; left: 40px; top: 584px; width: 380px;
    list-style: none; font-size: 13.2px; line-height: 16.5px; color: #222;
  }
  .services li { position: relative; padding-left: 24px; }
  .services svg { position: absolute; left: 0; top: 3px; }

  .call-box {
    position: absolute; left: 40px; top: 947px; width: 350px; height: 89px;
    border: 2.5px dashed #8c8c8c; border-radius: 9px; text-align: center;
  }
  .call-title {
    margin-top: 6px; font-size: 25px; font-weight: 700;
    color: var(--brand-blue); line-height: 30px;
  }
  .call-number {
    display: flex; justify-content: center; align-items: center; gap: 8px;
    font-size: 35px; font-weight: 700; color: #222; line-height: 44px;
  }

  .photo-frame {
    position: absolute; left: 420px; width: 389px; height: 289px;
    border: 3px solid var(--frame-grey); padding: 3px; background: #fff;
  }
  .photo { width: 100%; height: 100%; }
  .frame-1 { top: 127px; }
  .frame-2 { top: 435px; }
  .frame-3 { top: 743px; }
  .photo-wood { background: linear-gradient(135deg, #8a7560 0%, #6f5d4b 50%, #9b8670 100%); }
  .photo-white { background: linear-gradient(135deg, #cfcbc4 0%, #e6e3dd 55%, #b9b4ab 100%); }
  .photo-patina { background: linear-gradient(135deg, #9a7f78 0%, #8fa294 50%, #a58a80 100%); }

  .contact-band {
    position: absolute; left: 0; top: 1043px; width: 842px; height: 46px;
    background: linear-gradient(90deg, var(--brand-blue-dark), var(--brand-blue), var(--brand-blue-dark));
    color: #fff; font-size: 16.5px;
  }
  .contact-item { position: absolute; top: 0; height: 46px; display: flex; align-items: center; gap: 15px; }
  .contact-address { left: 90px; }
  .contact-email { left: 298px; }
  .contact-web { left: 553px; }
</style>
</head>
<body>
<div class="canvas">
  <article class="flyer">
    <div class="headline-band"></div>
    <h1 class="headline">LOREM IPSUM</h1>
    <div class="logo-name">YOUR LOGO</div>

    <h2 class="tag tag-about">ABOUT US</h2>
    <p class="about-text">Lorem Ipsum is simply dummy text of the printing and typesetting industry. Lorem Ipsum has been the industry's standard dummy text ever since the 1500s, when an unknown printer took a galley of type and scrambled it to make a type specimen book. It has survived not only five centuries, but also the leap into electronic typesetting, remaining essentially unchanged. It was popularised in the 1960s with the release of Typerex sheets containing Lorem Ipsum passages, and more recently with desktop publishing software like Quill PageSetter including versions of Lorem Ipsum.</p>

    <h2 class="tag tag-services">SERVICES:</h2>
    <ul class="services">
      <li style="margin-top:10px"><svg width="14" height="14" viewBox="0 0 14 14"><rect x="1" y="2" width="11" height="11" fill="none" stroke="#1d5fa6" stroke-width="1.4"/><path d="M3.5 7l2.5 2.5L13 2" fill="none" stroke="#1d5fa6" stroke-width="1.6"/></svg>The standard Lorem Ipsum passage, used since the 1500s</li>
      <li style="margin-top:11px"><svg width="14" height="14" viewBox="0 0 14 14"><rect x="1" y="2" width="11" height="11" fill="none" stroke="#1d5fa6" stroke-width="1.4"/><path d="M3.5 7l2.5 2.5L13 2" fill="none" stroke="#1d5fa6" stroke-width="1.6"/></svg>Section 1.10.32 of "de Finibus Bonorum et Malorum",<br>written by Tullan in 45 BC</li>
      <li style="margin-top:16px"><svg width="14" height="14" viewBox="0 0 14 14"><rect x="1" y="2" width="11" height="11" fill="none" stroke="#1d5fa6" stroke-width="1.4"/><path d="M3.5 7l2.5 2.5L13 2" fill="none" stroke="#1d5fa6" stroke-width="1.6"/></svg>1914 translation by H. Brantley</li>
      <li style="margin-top:16px"><svg width="14" height="14" viewBox="0 0 14 14"><rect x="1" y="2" width="11" height="11" fill="none" stroke="#1d5fa6" stroke-width="1.4"/><path d="M3.5 7l2.5 2.5L13 2" fill="none" stroke="#1d5fa6" stroke-width="1.6"/></svg>Section 1.10.33 of "de Finibus Bonorum et Malorum",<br>written by Tullan in 45 BC</li>
      <li style="margin-top:16px"><svg width="14" height="14" viewBox="0 0 14 14"><rect x="1" y="2" width="11" height="11" fill="none" stroke="#1d5fa6" stroke-width="1.4"/><path d="M3.5 7l2.5 2.5L13 2" fill="none" stroke="#1d5fa6" stroke-width="1.6"/></svg>1914 translation by H. Brantley</li>
      <li style="margin-top:16px"><svg width="14" height="14" viewBox="0 0 14 14"><rect x="1" y="2" width="11" height="11" fill="none" stroke="#1d5fa6" stroke-width="1.4"/><path d="M3.5 7l2.5 2.5L13 2" fill="none" stroke="#1d5fa6" stroke-width="1.6"/></svg>Section 1.10.33 of "de Finibus Bonorum et Malorum",<br>written by Tullan in 45 BC</li>
      <li style="margin-top:16px"><svg width="14" height="14" viewBox="0 0 14 14"><rect x="1" y="2" width="11" height="11" fill="none" stroke="#1d5fa6" stroke-width="1.4"/><path d="M3.5 7l2.5 2.5L13 2" fill="none" stroke="#1d5fa6" stroke-width="1.6"/></svg>1914 translation by H. Brantley</li>
      <li style="margin-top:10px"><svg width="14" height="14" viewBox="0 0 14 14"><rect x="1" y="2" width="11" height="11" fill="none" stroke="#1d5fa6" stroke-width="1.4"/><path d="M3.5 7l2.5 2.5L13 2" fill="none" stroke="#1d5fa6" stroke-width="1.6"/></svg>Section 1.10.32 of "de Finibus Bonorum et Malorum",<br>written by Tullan in 45 BC</li>
      <li style="margin-top:16px"><svg width="14" height="14" viewBox="0 0 14 14"><rect x="1" y="2" width="11" height="11" fill="none" stroke="#1d5fa6" stroke-width="1.4"/><path d="M3.5 7l2.5 2.5L13 2" fill="none" stroke="#1d5fa6" stroke-width="1.6"/></svg>1914 translation by H. Brantley</li>
    </ul>

    <div class="call-box">
      <div class="call-title">CALL US TODAY</div>
      <div class="call-number">
        <svg width="32" height="32" viewBox="0 0 32 32" aria-hidden="true">
          <path d="M9 4c1.5 0 4 5 4 6.5S10.5 13 10.5 14c0 2 5.5 7.5 7.5 7.5 1 0 2-2.5 3.5-2.5S28 21.5 28 23c0 2-3 5-6 5C14 28 4 18 4 10c0-3 3-6 5-6z" fill="none" stroke="#1d5fa6" stroke-width="2.6"/>
          <path d="M18 4a10 10 0 0 1 10 10M18 9a5 5 0 0 1 5 5" fill="none" stroke="#1d5fa6" stroke-width="2.2"/>
        </svg>
        <span>0123456789</span>
      </div>
    </div>

    <div class="photo-frame frame-1"><div class="photo photo-wood" role="img" aria-label="Photo: wrought iron scroll grille on a weathered wooden door"></div></div>
    <div class="photo-frame frame-2"><div class="photo photo-white" role="img" aria-label="Photo: iron strap hinge on a distressed white painted door"></div></div>
    <div class="photo-frame frame-3"><div class="photo photo-patina" role="img" aria-label="Photo: close-up of a door panel with peeling green and pink paint"></div></div>

    <footer class="contact-band">
      <div class="contact-item contact-address">
        <svg width="16" height="20" viewBox="0 0 16 20" aria-hidden="true"><path d="M8 1a6.5 6.5 0 0 0-6.5 6.5C1.5 12 8 19 8 19s6.5-7 6.5-11.5A6.5 6.5 0 0 0 8 1z" fill="#fff"/><circle cx="8" cy="7.5" r="2.6" fill="#1d5fa6"/></svg>
        <span>Address / Location</span>
      </div>
      <div class="contact-item contact-email">
        <svg width="18" height="13" viewBox="0 0 18 13" aria-hidden="true"><rect x="0.8" y="0.8" width="16.4" height="11.4" fill="none" stroke="#fff" stroke-width="1.5"/><path d="M1 1l8 6 8-6" fill="none" stroke="#fff" stroke-width="1.5"/></svg>
        <span>info@yourwebside.com</span>
      </div>
      <div class="contact-item contact-web">
        <svg width="16" height="16" viewBox="0 0 16 16" aria-hidden="true"><g fill="none" stroke="#fff" stroke-width="1.3"><circle cx="8" cy="8" r="7"/><ellipse cx="8" cy="8" rx="3" ry="7"/><path d="M1 8h14M2 4.5h12M2 11.5h12"/></g></svg>
        <span>www.yourwebside.com</span>
      </div>
    </footer>
  </article>
</div>
</body>
</html>
```